Custom Wordpress Theme Needed

We need a custom Wordpress theme built with the following features:

1. Flat style design
2. Fully responsive - built for mobile and tablets first; bootstrap or other framework used
3. Flexible - comes with homepage layouts for portfolios, agencies, and magazines
4. Built in 'contact' and 'about us' styling
5. Pre-populated pages and content, including reusable images
6. Multiple slider options

We are completely open to your creativity as far as the overall design style is concerned, but some of our favorites are:
http://themes.plovarek.com/themeselector/?theme=TideBoard
http://www.gorvelta.ru/levelpress/
http://layoutquarry.com/wp/vesk/intro/
http://theme.brindolaq.net/second/

Most unique and in-depth style wins!

Reason: We need more designs!

Reason: Waiting on final submissions and revisions. Thanks!

```html
<!DOCTYPE html>
<html lang="en">
<head>
<meta charset="utf-8">
<title>Corvin Hale</title>
<link href="https://fonts.googleapis.com/css2?family=Open+Sans:ital,wght@0,400;0,600;0,700;1,400&display=swap" rel="stylesheet">
<style>
:root{
  --ink:#2b2b2b;
  --text:#555;
  --muted:#8a8a8a;
  --line:#e2e2e2;
  --teal:#4d7d8f;
  --teal-band:#5b8796;
  --button:#5f8796;
  --nav:#2a2a2a;
  --footer:#2d2d2d;
  --paper:#ffffff;
  --soft:#f2f2f2;
}
*{box-sizing:border-box;margin:0;padding:0}
html,body{width:1200px;height:2616px;overflow:hidden;background:var(--paper)}
body{font-family:"Open Sans",Arial,sans-serif;color:var(--text);position:relative}
.abs{position:absolute}
.fill{display:block}

/* top bar */
.topbar{left:0;top:0;width:1200px;height:57px;background:var(--nav);z-index:2}
.brand{left:182px;top:12px;color:#fff;font-size:24px;font-weight:700;letter-spacing:-0.5px}
.mainnav{right:160px;top:0;display:flex;gap:0;height:57px;align-items:center}
.mainnav a{color:#d6d6d6;text-decoration:none;font-size:10px;font-weight:600;margin-left:43px;letter-spacing:.3px}

/* hero */
.hero{left:0;top:57px;width:1200px;height:529px;background:linear-gradient(180deg,#6b6b6b 0%,#9a9a9a 28%,#4a4a4a 55%,#1a1a1a 100%)}
.hero-arrow{top:278px;width:44px;height:44px;border-radius:50%;border:2px solid rgba(255,255,255,.35)}
.hero-title{left:0;width:1200px;top:376px;text-align:center;color:#fff;font-size:25px;font-weight:600;letter-spacing:.2px}
.hero-sub{left:0;width:1200px;text-align:center;color:#eee}
.hero-btn{left:480px;top:488px;width:240px;height:52px;border:1px solid #e8e8e8;color:#fff;font-size:16px;display:flex;align-items:center;justify-content:center}

/* welcome */
.welcome-title{left:0;width:1200px;top:612px;text-align:center;color:var(--teal);font-size:18px;font-weight:700}
.welcome-text{left:0;width:1200px;text-align:center}
.outline-btn{left:460px;top:717px;width:276px;height:38px;border:1px solid #cfcfcf;color:var(--ink);font-size:12px;display:flex;align-items:center;justify-content:center}

/* feature tiles */
.feature{top:799px;width:268px;height:174px}
.feature p{position:absolute;left:18px;bottom:14px;color:#fff;font-size:11.5px;line-height:17px}

/* section headings */
.section-title{color:var(--ink);font-size:17px;font-weight:600}
.rule{height:1px;background:var(--line)}

/* article grid */
.articles{left:180px;top:1048px;display:grid;grid-template-columns:repeat(3,178px);column-gap:10px;row-gap:17px}
.card{height:249px;border:1px solid #ececec;background:var(--paper);position:relative}
.card.is-active{background:var(--soft)}
.card .thumb{height:121px}
.card h3{font-size:10px;font-weight:700;color:var(--ink);margin:12px 0 0 14px}
.card .excerpt{font-size:9px;line-height:16px;color:var(--muted);margin:6px 14px 0 14px}
.card .date{font-size:9px;font-style:italic;color:var(--ink);margin:6px 0 0 14px}
.card .date u{text-decoration:underline}
.card .meta{position:absolute;left:0;right:0;bottom:0;height:30px;border-top:1px solid #ececec;display:flex;align-items:center;padding:0 14px;font-size:8.5px;font-style:italic;color:var(--muted)}
.card .meta svg{margin-right:6px}
.stars{margin-left:auto;font-style:normal;letter-spacing:1px;font-size:10px;color:#3a3a3a}
.stars i{font-style:normal;color:#c8c8c8}

.btn{background:var(--button);color:#fff;font-size:11px;display:flex;align-items:center;justify-content:center;border-radius:2px}

/* photo sets */
.photos{left:180px;top:1955px;display:grid;grid-template-columns:repeat(3,181px);grid-auto-rows:128px;column-gap:7px;row-gap:10px}

/* sidebar */
.cat-list{left:780px;top:1043px;width:240px;list-style:none}
.cat-list li{height:32.6px;border-bottom:1px solid #ededed;font-size:9px;color:#666;display:flex;align-items:center;padding-left:2px}
.cat-list li:before{content:"›";font-size:13px;color:#888;margin-right:10px}
.ad{left:764px;top:1291px;width:256px;height:212px;background:linear-gradient(135deg,#6a2a7a 0%,#8a3a8a 45%,#d9a23a 100%)}
.tabs{left:764px;top:1526px;width:256px;height:33px;display:flex;border-bottom:3px solid var(--teal)}
.tabs span{flex:1;display:flex;align-items:center;justify-content:center;font-size:11px;background:#e6e6e6;color:#666;border-right:1px solid #fff}
.tabs span.on{background:var(--teal);color:#fff}
.pop{left:764px;width:256px;height:88px;border-bottom:1px solid #ececec}
.pop .thumb{position:absolute;left:3px;top:8px;width:84px;height:68px;border:2px solid #ddd}
.pop h4{position:absolute;left:106px;top:8px;width:150px;font-size:8.5px;line-height:14px;color:var(--teal);font-weight:600}
.pop p{position:absolute;left:106px;top:40px;width:150px;font-size:8.5px;line-height:14px;color:#777}

.social-box{left:764px;top:1925px;width:256px;height:264px;background:#efefef;border:1px solid #e4e4e4}
.sb-logo{left:16px;top:14px;width:40px;height:40px;background:#3f5f2f}
.sb-name{left:66px;top:14px;font-size:11px;font-weight:700;color:#3b5a8a}
.sb-like{left:66px;top:36px;width:62px;height:16px;border:1px solid #bfc8d8;background:#f6f7f9;font-size:8px;color:#3b5a8a;display:flex;align-items:center;justify-content:center}
.sb-count{left:16px;top:72px;font-size:8.5px;color:#555}
.sb-faces{left:16px;top:95px;display:grid;grid-template-columns:repeat(6,34px);grid-auto-rows:34px;gap:4px}
.sb-faces div{width:34px;height:34px}
.sb-foot{left:16px;top:242px;font-size:8px;color:#777}

.tags{left:764px;top:2270px;width:256px;display:flex;flex-wrap:wrap;gap:6px 5px}
.tags span{background:#2d2d2d;color:#fff;font-size:8.5px;height:22px;padding:0 7px;display:flex;align-items:center}

/* bottom band */
.band{left:0;top:2442px;width:1200px;height:75px;background:var(--teal-band)}
.band p{position:absolute;left:182px;top:29px;color:#fff;font-size:9.5px;font-weight:600}
.band .outline{position:absolute;left:839px;top:20px;width:166px;height:36px;border:1px solid #fff;color:#fff;font-size:9.5px;display:flex;align-items:center;justify-content:center}

.footer{left:0;top:2517px;width:1200px;height:99px;background:var(--footer)}
.footnav{position:absolute;left:182px;top:30px;display:flex;font-size:8.5px;color:#ddd}
.footnav span{padding:0 21px;border-left:1px solid #777}
.footnav span:first-child{padding-left:0;border-left:0}
.copy{position:absolute;left:182px;top:58px;font-size:8px;color:#bbb}
.socials{position:absolute;left:844px;top:40px;display:flex;gap:5px}
.socials span{width:18px;height:18px;border-radius:50%;background:#5a5a5a}
</style>
</head>
<body>

<header class="abs topbar">
  <div class="abs brand">Corvinhale</div>
  <nav class="abs mainnav">
    <a>HOME</a><a>GALLERY</a><a>FEATURES</a><a>PAGES</a><a>ARCHIVE</a><a>BUSINESS</a><a>TRAVEL</a>
  </nav>
</header>

<section class="abs hero" role="img" aria-label="Black and white night city skyline beside a suspension bridge over the river"></section>
<div class="abs hero-arrow" style="left:64px"></div>
<div class="abs hero-arrow" style="left:1076px"></div>
<h1 class="abs hero-title">DEFAULT MODEL TEXT, AND A SEARCH FOR WEB SITES STILL</h1>
<p class="abs hero-sub" style="top:425px;font-size:14px">Default model text, and a search for 'lorem ipsum' will uncover many web sites still in their infancy.</p>
<p class="abs hero-sub" style="top:450px;font-size:11.5px">Various versions have evolved over the years, sometimes by accident, sometimes on purpose</p>
<div class="abs hero-btn">JOIN TO OUR TEAM</div>

<h2 class="abs welcome-title">WELCOME TO CORVIN HALE</h2>
<p class="abs welcome-text" style="top:654px;font-size:13px;color:#444">Default model text, and a search for 'lorem ipsum' will uncover many web sites still in their infancy.</p>
<p class="abs welcome-text" style="top:679px;font-size:11px;color:#666">Various versions have evolved over the years, sometimes by accident, sometimes on purpose</p>
<div class="abs outline-btn">CLICK HERE FOR MORE INFORMATION</div>

<div class="abs feature" style="left:180px;background:linear-gradient(180deg,#bdbdbd,#3e3e3e)" role="img" aria-label="Plane flying over a rider on a motorbike under a cloudy sky"><p>Default model text, and a search for<br>uncover many web sites still in their infancy.</p></div>
<div class="abs feature" style="left:467px;background:linear-gradient(160deg,#5a3418,#b87a3a 55%,#2a170a)" role="img" aria-label="Hands shaping clay on a pottery wheel"><p>Default model text, and a search for<br>uncover many web sites still in their infancy.</p></div>
<div class="abs feature" style="left:753px;background:linear-gradient(180deg,#f0c47a,#d48a3a 60%,#3a2410)" role="img" aria-label="Silhouette of a dancer against a sunset sky"><p>Default model text, and a search for<br>uncover many web sites still in their infancy.</p></div>

<h2 class="abs section-title" style="left:180px;top:991px">Latest Articles</h2>
<div class="abs rule" style="left:180px;top:1029px;width:561px"></div>

<div class="abs articles">
  <article class="card is-active"><div class="thumb fill" style="background:linear-gradient(180deg,#d99a5a,#8a5a30)" role="img" aria-label="Waves on a sandy beach at sunset"></div><h3>Orci ipsum, placerat id</h3><p class="excerpt">Various versions have evolved over the years, sometimes.</p><p class="date">Posted on <u>27 Aug 2013</u></p><div class="meta"><svg width="10" height="9" viewBox="0 0 10 9"><path d="M0 0h10v6H4L1 9V6H0z" fill="#555"/></svg>102 Comments<span class="stars">★★<i>★★★</i></span></div></article>
  <article class="card"><div class="thumb fill" style="background:linear-gradient(135deg,#2a2a2a,#9a9a9a)" role="img" aria-label="Black and white portrait"></div><h3>Orci ipsum, placerat id</h3><p class="excerpt">Various versions have evolved over the years, sometimes.</p><p class="date">Posted on <u>27 Aug 2013</u></p><div class="meta"><svg width="10" height="9" viewBox="0 0 10 9"><path d="M0 0h10v6H4L1 9V6H0z" fill="#555"/></svg>102 Comments<span class="stars">★★<i>★★★</i></span></div></article>
  <article class="card"><div class="thumb fill" style="background:linear-gradient(135deg,#3a2a1e,#8a6a4a)" role="img" aria-label="Vintage camera on a wooden table"></div><h3>Orci ipsum, placerat id</h3><p class="excerpt">Various versions have evolved over the years, sometimes.</p><p class="date">Posted on <u>27 Aug 2013</u></p><div class="meta"><svg width="10" height="9" viewBox="0 0 10 9"><path d="M0 0h10v6H4L1 9V6H0z" fill="#555"/></svg>102 Comments<span class="stars">★★<i>★★★</i></span></div></article>

  <article class="card"><div class="thumb fill" style="background:linear-gradient(180deg,#6a9a3a,#3a6a1a)" role="img" aria-label="Child resting on a green lawn"></div><h3>Orci ipsum, placerat id</h3><p class="excerpt">Various versions have evolved over the years, sometimes.</p><p class="date">Posted on <u>27 Aug 2013</u></p><div class="meta"><svg width="10" height="9" viewBox="0 0 10 9"><path d="M0 0h10v6H4L1 9V6H0z" fill="#555"/></svg>102 Comments<span class="stars">★★<i>★★★</i></span></div></article>
  <article class="card"><div class="thumb fill" style="background:linear-gradient(180deg,#8a7a5a,#2a2418)" role="img" aria-label="Street lamp against a dramatic sky"></div><h3>Orci ipsum, placerat id</h3><p class="excerpt">Various versions have evolved over the years, sometimes.</p><p class="date">Posted on <u>27 Aug 2013</u></p><div class="meta"><svg width="10" height="9" viewBox="0 0 10 9"><path d="M0 0h10v6H4L1 9V6H0z" fill="#555"/></svg>102 Comments<span class="stars">★★<i>★★★</i></span></div></article>
  <article class="card"><div class="thumb fill" style="background:linear-gradient(180deg,#9aa05a,#c8a04a 60%,#5a4a2a)" role="img" aria-label="Classic car parked in a field"></div><h3>Orci ipsum, placerat id</h3><p class="excerpt">Various versions have evolved over the years, sometimes.</p><p class="date">Posted on <u>27 Aug 2013</u></p><div class="meta"><svg width="10" height="9" viewBox="0 0 10 9"><path d="M0 0h10v6H4L1 9V6H0z" fill="#555"/></svg>102 Comments<span class="stars">★★<i>★★★</i></span></div></article>

  <article class="card"><div class="thumb fill" style="background:linear-gradient(135deg,#1a1a1a,#7a7a7a)" role="img" aria-label="Black and white close up of small feet"></div><h3>Orci ipsum, placerat id</h3><p class="excerpt">Various versions have evolved over the years, sometimes.</p><p class="date">Posted on <u>27 Aug 2013</u></p><div class="meta"><svg width="10" height="9" viewBox="0 0 10 9"><path d="M0 0h10v6H4L1 9V6H0z" fill="#555"/></svg>102 Comments<span class="stars">★★<i>★★★</i></span></div></article>
  <article class="card"><div class="thumb fill" style="background:linear-gradient(180deg,#a8a8a8,#4a4a4a)" role="img" aria-label="Black and white busy street scene"></div><h3>Orci ipsum, placerat id</h3><p class="excerpt">Various versions have evolved over the years, sometimes.</p><p class="date">Posted on <u>27 Aug 2013</u></p><div class="meta"><svg width="10" height="9" viewBox="0 0 10 9"><path d="M0 0h10v6H4L1 9V6H0z" fill="#555"/></svg>102 Comments<span class="stars">★★<i>★★★</i></span></div></article>
  <article class="card"><div class="thumb fill" style="background:linear-gradient(180deg,#3a3a3a,#bdbdbd)" role="img" aria-label="Cyclist riding through a water spray"></div><h3>Orci ipsum, placerat id</h3><p class="excerpt">Various versions have evolved over the years, sometimes.</p><p class="date">Posted on <u>27 Aug 2013</u></p><div class="meta"><svg width="10" height="9" viewBox="0 0 10 9"><path d="M0 0h10v6H4L1 9V6H0z" fill="#555"/></svg>102 Comments<span class="stars">★★<i>★★★</i></span></div></article>
</div>

<div class="abs btn" style="left:607px;top:1849px;width:129px;height:29px">View more Posts</div>

<h2 class="abs section-title" style="left:180px;top:1899px">Photo Sets</h2>
<div class="abs photos">
  <div style="background:linear-gradient(135deg,#c8b05a,#6a7a2a)" role="img" aria-label="Sunlit outdoor portrait"></div>
  <div style="background:linear-gradient(180deg,#1a6a9a,#0a2a4a)" role="img" aria-label="Dog swimming underwater"></div>
  <div style="background:linear-gradient(135deg,#d8a85a,#3a4a5a)" role="img" aria-label="Person with a tattooed arm"></div>
  <div style="background:linear-gradient(135deg,#e8e8e8,#7a3a2a)" role="img" aria-label="Bride beside a red vintage car"></div>
  <div style="background:linear-gradient(180deg,#d8b890,#3a4a6a)" role="img" aria-label="Couple in front of historic buildings"></div>
  <div style="background:linear-gradient(180deg,#b8b8b8,#3a3a3a)" role="img" aria-label="Boats on a misty lake"></div>
  <div style="background:linear-gradient(180deg,#9a9a9a,#2a2a2a)" role="img" aria-label="Man wading in dark water"></div>
  <div style="background:linear-gradient(180deg,#c8a878,#3a2a1a)" role="img" aria-label="Bare tree branches over a lake"></div>
  <div style="background:linear-gradient(135deg,#5a8a3a,#c8a06a)" role="img" aria-label="Photographer holding a camera"></div>
</div>
<div class="abs btn" style="left:607px;top:2379px;width:129px;height:30px">View more Posts</div>

<!-- sidebar -->
<h2 class="abs section-title" style="left:780px;top:1003px">Categories</h2>
<div class="abs rule" style="left:780px;top:1039px;width:240px"></div>
<ul class="abs cat-list">
  <li>Advertising (2)</li><li>Business (6)</li><li>Design (2)</li><li>Mobile devices (1)</li><li>Travel (4)</li><li>Uncategorized (2)</li><li>Web Development (1)</li>
</ul>

<div class="abs ad" role="img" aria-label="Banner advertisement for an antioxidant supplement"></div>

<div class="abs tabs"><span class="on">Popular</span><span>Recent</span><span>Relavent</span></div>
<div class="abs pop" style="top:1570px"><div class="thumb" style="background:linear-gradient(180deg,#e8c890,#8a5a2a)" role="img" aria-label="Rock at sunset"></div><h4>DEFAULT MODEL TEXT, AND A SEARCH</h4><p>Default model text, and a search for 'lorem ipsum' will uncover...</p></div>
<div class="abs pop" style="top:1670px"><div class="thumb" style="background:linear-gradient(135deg,#2a2a2a,#b0b0b0)" role="img" aria-label="Black and white abstract close up"></div><h4>DEFAULT MODEL TEXT, AND A SEARCH</h4><p>Default model text, and a search for 'lorem ipsum' will uncover...</p></div>
<div class="abs pop" style="top:1769px"><div class="thumb" style="background:linear-gradient(180deg,#d0d0d0,#3a3a3a)" role="img" aria-label="Silhouette figure on a light background"></div><h4>DEFAULT MODEL TEXT, AND A SEARCH</h4><p>Default model text, and a search for 'lorem ipsum' will uncover...</p></div>
<div class="abs btn" style="left:764px;top:1873px;width:129px;height:28px">View more Posts</div>

<aside class="abs social-box">
  <div class="abs sb-logo"></div>
  <div class="abs sb-name">Tessora</div>
  <div class="abs sb-like">Like page</div>
  <div class="abs sb-count">29 192 people like Tessora.</div>
  <div class="abs sb-faces">
    <div style="background:#7a8a9a" role="img" aria-label="Follower avatar"></div><div style="background:#a08060" role="img" aria-label="Follower avatar"></div><div style="background:#5a7aa0" role="img" aria-label="Follower avatar"></div><div style="background:#9aa07a" role="img" aria-label="Follower avatar"></div><div style="background:#c0a0a0" role="img" aria-label="Follower avatar"></div><div style="background:#8a8a8a" role="img" aria-label="Follower avatar"></div>
    <div style="background:#5aa0b0" role="img" aria-label="Follower avatar"></div><div style="background:#b08a6a" role="img" aria-label="Follower avatar"></div><div style="background:#3a6a9a" role="img" aria-label="Follower avatar"></div><div style="background:#c89a3a" role="img" aria-label="Follower avatar"></div><div style="background:#9a9a9a" role="img" aria-label="Follower avatar"></div><div style="background:#6a5a4a" role="img" aria-label="Follower avatar"></div>
    <div style="background:#6aa0c8" role="img" aria-label="Follower avatar"></div><div style="background:#c8d0e0" role="img" aria-label="Follower avatar"></div><div style="background:#4a6a8a" role="img" aria-label="Follower avatar"></div><div style="background:#8a7aa0" role="img" aria-label="Follower avatar"></div><div style="background:#a0704a" role="img" aria-label="Follower avatar"></div><div style="background:#3a3a3a" role="img" aria-label="Follower avatar"></div>
  </div>
  <div class="abs sb-foot">Social plugin · Linkwall</div>
</aside>

<h2 class="abs section-title" style="left:764px;top:2210px">Tags</h2>
<div class="abs rule" style="left:764px;top:2249px;width:256px"></div>
<div class="abs tags">
  <span>audio</span><span>blog</span><span>corporate</span><span>internet</span>
  <span>news</span><span>photography</span><span>responsive</span>
  <span>travel</span><span>video</span><span>webdesign</span>
</div>

<section class="abs band">
  <p>DEFAULT MODEL TEXT, AND A SEARCH FOR 'LOREM IPSUM' WILL UNCOVER MANY WEB SITES STILL IN THEIR INFANCY. VARIOUS VERSIONS...</p>
  <div class="outline">CLICK HERE FOR JOIN NOW</div>
</section>

<footer class="abs footer">
  <div class="footnav"><span>HOME</span><span>GALLERY</span><span>FEATURES</span><span>PAGES</span><span>ARCHIVE</span><span>BUSINESS</span><span>TRAVEL</span></div>
  <div class="copy">© COPYRIGHT 2013. CORVIN HALE. ALL RIGHTS RESERVED.</div>
  <div class="socials"><span></span><span></span><span></span><span></span><span></span><span></span><span></span><span></span></div>
</footer>

</body>
</html>
```